Non-Profit Needs Plastic Recycling Infographic

We need a modern infographic to help illustrate international recycling rates for expanded polystyrene plastic. Include the information below and use the attached PowerPoint as an example for your design – the PowerPoint is just to illustrate the information; you do not need to follow it completely.

We have also included our updated color guide.

Please fit the following information into the infographic:
• The one item that is necessary is the global map – the "Global EPS Packaging Recycling" header is not required
• Do NOT include any "chasing arrows" recycling symbols
• the "34 Countries" should read "34 Countries with a Confirmed Recycling Rate"
• "34 Countries" should be an information block along with the "21 Countries"
• The "32 Countries" and "62 Countries" should be included in the graph image – we have given a pie graph as an example, though it can be another graph
• "Leading EPS Recyclate Sources" should have the following four blocks associated with it: Automotive, Seafood & Fishers, Furniture, and Appliances; use attached photos for blocks
• The lorem ipsum vertical information blocks should include 3 columns:
#1: "Developing Countries Recycle EPS" – include country outline of Guatemala; include the text "EPS manufacturing is working with government in Guatemala. Where an EPS molder exists is the easiest way to initiate EPS recycling. Work with the EPS manufacturing sector can promote quick startup of B2B recycling programs."
#2: "Small Islands Recycle EPS" – include country outline of Dominican Republic; include the text "An EPS recycling program in the Dominican Republic highlighted the need for new polystyrene recycling technologies. Through their work with machinery specialists, they were able to identify a solution that then spread to other nations."
#3: "Local Communities Recycle EPS" – include country outline of China; include text "EPS startups can lead to successful recycling collection programs. Lanfeng Neighborhood Office in Xiamen City, China, was already receiving polystyrene for recycling when they were able to procure a densifier. Since installation, the program has spread to five machines located across the city."
• Under the "Unified Resource Stewardship Compact" statement, include the following: "Criteria could be tailored to specific applications, allowing for country-specific flexibility. This approach would also help to develop standards on a material basis and allow countries to focus on scientific research and assess availability of recycling programs."

Font styles to use
Sans Serif

Requirements
Must have
• 1. Global EPS Recycling Map (see attached documents), 2. Infographic should be vertical in design, NOT horizontal
Should not have
• Chasing Arrows Recycling Symbols

```html
<!DOCTYPE html>
<html lang="en">
<head>
<meta charset="utf-8">
<title>Foamcycle Alliance – EPS Recycling Around the World</title>
<link href="https://fonts.googleapis.com/css2?family=Bebas+Neue&family=Open+Sans:wght@300;400;600;700&display=swap" rel="stylesheet">
<style>
  :root {
    --cream: #fffdf5;
    --navy: #152a4e;
    --orange: #f07e52;
    --gold: #b8930f;
    --yellow: #f0ae2f;
    --slate: #535353;
    --olive: #a1ae3a;
    --mist: #e3dfe0;
    --brown: #5a2e1a;
    --white: #ffffff;
  }
  * { box-sizing: border-box; margin: 0; padding: 0; }
  html, body { width: 768px; height: 1200px; overflow: hidden; background: var(--cream); }
  body { font-family: "Open Sans", Arial, sans-serif; color: var(--navy); }
  .canvas { position: relative; width: 768px; height: 1200px; background: var(--cream); overflow: hidden; }
  .abs { position: absolute; }
  .display { font-family: "Bebas Neue", "Oswald", sans-serif; font-weight: 400; }

  /* header */
  .brand-dot { left: 36px; top: 33px; width: 78px; height: 78px; border-radius: 50%; background: var(--gold); }
  .brand-name { left: 124px; top: 58px; font-size: 22px; font-weight: 400; color: var(--gold); letter-spacing: .2px; }
  .site-pill { left: 445px; top: 47px; width: 279px; height: 37px; border: 1px solid var(--gold); border-radius: 19px;
    display: flex; align-items: center; justify-content: center; font-size: 18px; font-weight: 700; color: var(--brown); }

  /* map (drawn first, stats sit above it) */
  .world-map { left: 232px; top: 146px; width: 528px; height: 268px; border-radius: 8px;
    background: linear-gradient(120deg, var(--olive) 0%, var(--mist) 45%, var(--mist) 65%, var(--navy) 100%); opacity: .85;
    clip-path: polygon(0 0, 100% 0, 100% 100%, 124px 100%, 124px 138px, 0 138px); z-index: 1; }
  .map-key { left: 223px; top: 419px; width: 523px; height: 17px; border-bottom: 1px solid #c9c6c0;
    display: flex; align-items: center; font-size: 8.5px; color: #6b6b6b; font-weight: 300; }
  .map-key .info { font-weight: 700; color: var(--navy); font-size: 9px; display: flex; align-items: center; gap: 5px; width: 57px; }
  .map-key .tri { width: 0; height: 0; border-left: 6px solid var(--navy); border-top: 5px solid transparent; border-bottom: 5px solid transparent; }
  .map-key .swatch { width: 13px; height: 13px; margin-right: 13px; }
  .map-key .item { display: flex; align-items: center; }
  .map-key b.olive { color: var(--olive); }
  .map-key b.navy { color: var(--navy); }

  /* stats */
  .stats > * { z-index: 2; }
  .stat-number { font-size: 64px; line-height: 1; letter-spacing: -1px; color: var(--navy); }
  .stat-label { font-size: 14.5px; line-height: 14.5px; color: var(--navy); }
  .stat-divider { left: 45px; top: 285px; width: 84px; height: 1px; background: var(--gold); opacity: .7; }
  .donut { left: 165px; top: 298px; }
  .pct-number { left: 265px; top: 302px; font-size: 34px; line-height: 1; }
  .pct-label { left: 265px; top: 334px; font-size: 13px; line-height: 12px; }
  .legend { left: 168px; top: 379px; font-size: 10.5px; font-weight: 700; line-height: 14px; }
  .legend li { list-style: none; display: flex; align-items: center; gap: 6px; }
  .legend i { display: inline-block; width: 7px; height: 7px; border-radius: 50%; }
  .legend .none { color: var(--orange); }
  .legend .none i { background: var(--orange); }
  .legend .yes i { background: var(--navy); }

  /* sources band */
  .sources-band { left: 0; top: 467px; width: 768px; height: 210px; background: var(--orange); }
  .sources-title { left: 35px; top: 487px; }
  .sources-title-text { left: 52px; top: 500px; font-size: 22.5px; line-height: 28px; color: var(--white); }
  .source { width: 100px; text-align: center; }
  .source-photo { width: 90px; height: 90px; margin: 0 auto; border-radius: 50%; border: 3px solid var(--yellow); }
  .source-label { margin-top: 5px; font-size: 12.5px; color: var(--navy); white-space: nowrap; }
  .sources-copy { left: 41px; top: 609px; width: 700px; font-size: 12.8px; line-height: 15.3px; color: var(--navy);
    letter-spacing: -0.25px; }

  /* case columns */
  .outline { height: 44px; border-radius: 14px 20px 10px 22px; }
  .case-bar { width: 216px; height: 59px; border-radius: 10px; display: flex; align-items: center; justify-content: center;
    text-align: center; font-size: 13px; font-weight: 700; line-height: 17.5px; }
  .case-num { width: 32px; height: 32px; border-radius: 50%; border: 2px solid var(--white); display: flex; align-items: center;
    justify-content: center; font-family: "Bebas Neue", sans-serif; font-size: 20px; color: var(--white); }
  .case-body { width: 216px; height: 202px; border-radius: 14px; padding: 11px 8px; text-align: center;
    font-size: 13px; line-height: 17.6px; font-weight: 300; letter-spacing: -0.1px; }
  .is-slate { background: var(--slate); color: var(--white); }
  .is-navy { background: var(--navy); color: var(--white); }
  .is-yellow { background: var(--yellow); color: var(--navy); }
  .is-yellow.case-body { font-weight: 400; letter-spacing: -0.3px; }

  /* compact band */
  .compact-band { left: 0; top: 1048px; width: 768px; height: 152px; background: var(--navy); }
  .compact-title { left: 60px; top: 1066px; width: 660px; font-size: 14.2px; line-height: 19px; font-weight: 700; color: var(--yellow); }
  .compact-copy { left: 59px; top: 1112px; width: 640px; font-size: 12.6px; line-height: 17.5px; color: var(--white); font-weight: 300; }
</style>
</head>
<body>
<main class="canvas">

  <header>
    <div class="abs brand-dot"></div>
    <div class="abs brand-name">Foamcycle Alliance</div>
    <div class="abs site-pill">www.foamcyclealliance.org</div>
  </header>

  <section class="map">
    <div class="abs world-map" role="img" aria-label="World map shading countries by EPS post-use recycling rate"></div>
    <div class="abs map-key">
      <span class="info"><span class="tri"></span>INFO:</span>
      <span class="item" style="width:185px;"><span class="swatch" style="background:var(--olive);"></span>Post - Use Recycling&nbsp;<b class="olive">Above 30%</b></span>
      <span class="item" style="width:162px;"><span class="swatch" style="background:var(--navy);"></span>Post - Use Recycling&nbsp;<b class="navy">10-30%</b></span>
      <span class="item"><span class="swatch" style="background:var(--mist);"></span>No information available</span>
    </div>
  </section>

  <section class="stats">
    <div class="abs display stat-number" style="left:45px; top:163px;">34</div>
    <div class="abs display stat-label" style="left:47px; top:215px;">Countries<br>with a confirmed<br>recycling rate</div>

    <div class="abs display stat-number" style="left:162px; top:163px;">62</div>
    <div class="abs display stat-label" style="left:163px; top:213px;">Countries<br>recycles EPS</div>

    <div class="abs stat-divider"></div>

    <div class="abs display stat-number" style="left:44px; top:306px;">21</div>
    <div class="abs display stat-label" style="left:45px; top:358px;">Countries have a<br>recycling rate<br>above 30%</div>

    <svg class="abs donut" width="140" height="80" viewBox="0 0 140 80" aria-label="32% of countries have EPS recycling">
      <g transform="translate(37 37) rotate(-90)">
        <circle r="31" fill="none" stroke="var(--orange)" stroke-width="9"/>
        <circle r="31" fill="none" stroke="var(--navy)" stroke-width="9" stroke-dasharray="62.3 132.5"/>
      </g>
      <polyline points="63,20 80,1 139,1" fill="none" stroke="var(--navy)" stroke-width="1.2"/>
    </svg>
    <div class="abs display pct-number">32%</div>
    <div class="abs display pct-label">Of countries<br>have EPS recycling</div>

    <ul class="abs legend">
      <li class="none"><i></i>No EPS Recycling</li>
      <li class="yes"><i></i>EPS Recycling</li>
    </ul>
  </section>

  <section class="sources">
    <div class="abs sources-band"></div>
    <svg class="abs sources-title" width="178" height="110" viewBox="0 0 178 110" aria-hidden="true">
      <path d="M10 0 H135 L176 55 L135 109 H10 Q0 109 0 99 V10 Q0 0 10 0 Z" fill="var(--navy)"/>
    </svg>
    <div class="abs display sources-title-text">Leading<br>EPS recyclate<br>sources</div>

    <figure class="abs source" style="left:249px; top:487px;">
      <div class="source-photo" role="img" aria-label="White EPS packaging insert for automotive parts" style="background:linear-gradient(135deg,#f4f4f4,#c9cbcf);"></div>
      <figcaption class="display source-label">Automotive</figcaption>
    </figure>
    <figure class="abs source" style="left:355px; top:487px;">
      <div class="source-photo" role="img" aria-label="Fresh fish packed in a white EPS cooler box" style="background:linear-gradient(160deg,#a9b3bd,#eef0f2);"></div>
      <figcaption class="display source-label">Seafood &amp; Fishers</figcaption>
    </figure>
    <figure class="abs source" style="left:465px; top:487px;">
      <div class="source-photo" role="img" aria-label="Cross-section of a truck bumper with EPS foam core" style="background:linear-gradient(160deg,#7a7f86,#ece6ee);"></div>
      <figcaption class="display source-label">Automotive concepts</figcaption>
    </figure>
    <figure class="abs source" style="left:571px; top:487px;">
      <div class="source-photo" role="img" aria-label="Washing machine with EPS corner packaging" style="background:linear-gradient(160deg,#eeeeee,#bfc0c2);"></div>
      <figcaption class="display source-label">Appliances</figcaption>
    </figure>

    <p class="abs sources-copy">Automated manufacturing assembly parts packaging, cold chain shipping containers for fresh fish, bracing for furniture distribution &amp; packaging protection for appliances are key sources of EPS transport packaging being diverted from the landfill or otherwise mismanaged disposal practices.</p>
  </section>

  <section class="cases">
    <div class="abs outline" role="img" aria-label="Outline of Guatemala" style="left:130px; top:696px; width:40px; background:var(--slate);"></div>
    <div class="abs outline" role="img" aria-label="Outline of the Dominican Republic" style="left:346px; top:696px; width:72px; background:var(--navy);"></div>
    <div class="abs outline" role="img" aria-label="Outline of China" style="left:586px; top:696px; width:54px; background:var(--yellow);"></div>

    <div class="abs case-bar is-slate" style="left:47px; top:747px;">Developing Countries<br>Recycle EPS</div>
    <div class="abs case-num" style="left:29px; top:759px; background:var(--slate);">01</div>
    <div class="abs case-body is-slate" style="left:47px; top:819px;">EPS manufacturing is working with government in Guatemala. Where an EPS molder exists is the easiest way to initiate EPS recycling. Work with the EPS manufacturing sector can promote quick startup of B2B recycling programs</div>

    <div class="abs case-bar is-navy" style="left:273px; top:747px;">Small Islands<br>Recycle EPS</div>
    <div class="abs case-num" style="left:255px; top:759px; background:var(--navy);">02</div>
    <div class="abs case-body is-navy" style="left:273px; top:819px;">An EPS recycling program in the Dominican Republic highlighted the need for new polystyrene recycling technologies. Through their work with machinery specialists, they were able to identify a solution that then spread to other nations.</div>

    <div class="abs case-bar is-yellow" style="left:499px; top:747px;">Local Communities<br>Recycle EPS</div>
    <div class="abs case-num" style="left:480px; top:759px; background:var(--yellow);">03</div>
    <div class="abs case-body is-yellow" style="left:499px; top:819px; padding-top:9px;">EPS startups can lead to successful recycling collection programs. Lanfeng Neighborhood Office in Xiamen City, China, was already receiving polystyrene for recycling when they were able to procure a densifier. Since installation, the program has spread to five machines located across the city.</div>
  </section>

  <section class="compact">
    <div class="abs compact-band"></div>
    <h2 class="abs compact-title">The Unified Resource Stewardship Compact Will Facilitate Improved Data Collection Through Mandatory Reporting Guidelines.</h2>
    <p class="abs compact-copy">Criteria could be tailored to specific applications, allowing for country-specific flexibility. This approach would also help to develop standards on a material basis and allow countries to focus on scientific research and assess availability of recycling programs.</p>
  </section>

</main>
</body>
</html>
```